Shipping Box Design for Comic book and Superhero movie prop replica fabricator

Shipping box design for our company " Pixel Lanterns" which produces and sells high end props and replicas based on comic books, movies, and tv shows, for display and cosplay all over the world. We strive for the most accurate replicas and highest quality products. We provide great customer care and frequently design and build completely custom products for companies. I want the design to convey quality and a premium product while still being fun and imaginative. I want the box to help promote Pixel Lanterns as a memorable brand and encourage repeat business.I included some photos of a few products.Box size is 12in x 12in x 2in
Requirements
Must have
- Company Colors, Company Logo, name, and website
Nice to have
- The box is like a pizza box, so may have something that makes it fit that theme somehow

```html
<!DOCTYPE html>
<html lang="en">
<head>
<meta charset="utf-8">
<title>Pixel Lanterns – Shipping Box Lid</title>
<link href="https://fonts.googleapis.com/css2?family=Anton&family=Bebas+Neue&family=Montserrat:wght@500;700;900&display=swap" rel="stylesheet">
<style>
  :root {
    --ink: #0d0d0d;
    --paper: #ffffff;
    --red: #d6102f;
    --blue: #1f6dbd;
    --blue-deep: #1a3f86;
    --yellow: #f5d800;
    --halftone: #c9c9c9;
    --skin: #e3bf86;
    --badge-text: #dfe9f7;
  }
  * { margin: 0; padding: 0; box-sizing: border-box; }
  html, body { width: 1149px; height: 1200px; overflow: hidden; background: var(--paper); }
  .lid { position: relative; width: 1149px; height: 1200px; background: var(--paper); }

  .frame-shadow {
    position: absolute; left: 44px; top: 35px; width: 1080px; height: 1148px;
    background: var(--red);
  }
  .frame {
    position: absolute; left: 25px; top: 16px; width: 1080px; height: 1148px;
    background: var(--ink);
  }
  .panel { position: absolute; background: var(--paper); overflow: hidden; }

  .tagline-band {
    position: absolute; left: 40px; top: 38px; width: 1055px; height: 76px;
    background: var(--yellow);
    display: flex; align-items: center; justify-content: flex-end; padding-right: 36px;
    font-family: "Bebas Neue", sans-serif; font-size: 60px; letter-spacing: 6px; color: var(--ink);
  }
  .tagline-band .dot { display: inline-block; width: 10px; height: 10px; border-radius: 50%; background: var(--ink); margin: 0 14px; }

  .hero-panel { left: 40px; top: 130px; width: 1055px; height: 612px; }
  .burst-art {
    position: absolute; inset: 0;
    background: radial-gradient(ellipse at 50% 48%, #ffffff 0%, #f1f1f1 40%, var(--halftone) 80%, #9a9a9a 100%);
  }
  .mascot-art {
    position: absolute; left: 262px; top: 8px; width: 520px; height: 272px;
    background: linear-gradient(90deg, var(--blue) 0%, var(--blue) 40%, var(--red) 40%, var(--red) 75%, var(--skin) 100%);
    border-radius: 8px;
  }
  .brand-name {
    position: absolute; left: 0; right: 0; top: 288px; text-align: center;
    font-family: "Anton", sans-serif; font-weight: 400; color: var(--blue);
  }
  .brand-name .line-one { display: block; font-size: 158px; line-height: 158px; letter-spacing: 14px; }
  .brand-name .line-two { display: block; font-size: 124px; line-height: 124px; letter-spacing: 6px; }
  .since-line {
    position: absolute; left: 0; right: 0; top: 572px; text-align: center;
    font-family: "Montserrat", sans-serif; font-weight: 900; font-size: 35px; line-height: 36px; letter-spacing: 1px; color: var(--ink);
  }

  .badge { position: absolute; left: 4px; top: 2px; width: 345px; height: 345px; }
  .badge-text {
    position: absolute; left: 4px; top: 2px; width: 345px; height: 345px;
    display: flex; flex-direction: column; align-items: center; justify-content: center;
    font-family: "Anton", sans-serif; font-size: 54px; line-height: 1.08; color: var(--badge-text); letter-spacing: 3px;
    transform: rotate(-4deg);
  }

  .shout-panel { left: 40px; top: 757px; width: 498px; height: 366px; background: var(--blue); }
  .shout-art {
    position: absolute; left: 25px; top: 25px; width: 448px; height: 316px;
    background: radial-gradient(ellipse at 45% 55%, var(--red) 0%, var(--red) 55%, var(--blue-deep) 100%);
    border-radius: 40%;
  }

  .label-panel { left: 552px; top: 757px; width: 543px; height: 366px; }
  .label-art {
    position: absolute; inset: 0;
    background: linear-gradient(135deg, #cfcfcf 0%, #ffffff 45%, #ffffff 70%, #e6e6e6 100%);
  }
  .label-spot {
    position: absolute; left: 0; right: 0; top: 150px; text-align: center;
    font-family: "Montserrat", sans-serif; color: var(--ink);
  }
  .label-spot .rule { width: 270px; height: 2px; background: var(--ink); margin: 0 auto; }
  .label-spot .main {
    font-weight: 700; font-size: 34px; letter-spacing: 4px; margin-top: 6px; position: relative; display: inline-block;
  }
  .label-spot .main::before, .label-spot .main::after {
    content: "\2605"; position: absolute; top: 4px; font-size: 22px;
  }
  .label-spot .main::before { left: -42px; }
  .label-spot .main::after { right: -42px; }
  .label-spot .sub { font-weight: 500; font-size: 31px; letter-spacing: 2px; margin: -4px 0 6px; }
</style>
</head>
<body>
<main class="lid">
  <div class="frame-shadow"></div>
  <div class="frame"></div>

  <div class="tagline-band">
    <span class="dot"></span>COOL PROPS AND REPLICAS<span class="dot"></span>
  </div>

  <section class="panel hero-panel">
    <div class="burst-art" role="img" aria-label="Comic halftone background with radiating speed lines"></div>
    <div class="mascot-art" role="img" aria-label="Caped card-shaped superhero mascot with flowing blue cape"></div>
    <h1 class="brand-name"><span class="line-one">PIXEL</span><span class="line-two">LANTERNS</span></h1>
    <p class="since-line">SINCE 2015 - MADE IN USA</p>
  </section>

  <svg class="badge" viewBox="0 0 200 200" aria-hidden="true">
    <polygon fill="#0d0d0d" stroke="#d6102f" stroke-width="3"
      points="100,5 118,38 152,18 150,56 190,58 166,88 196,112 158,124 172,162 134,152 124,192 100,162 76,192 66,152 28,162 42,124 4,112 34,88 10,58 50,56 48,18 82,38"/>
  </svg>
  <div class="badge-text"><span>GOODIES</span><span>INSIDE</span></div>

  <section class="panel shout-panel">
    <div class="shout-art" role="img" aria-label="Comic burst with hand-lettered HEY! exclamation"></div>
  </section>

  <section class="panel label-panel">
    <div class="label-art" role="img" aria-label="Soft halftone fade"></div>
    <div class="label-spot">
      <div class="rule"></div>
      <div class="main">SHIPPING</div>
      <div class="sub">LABEL HERE</div>
      <div class="rule"></div>
    </div>
  </section>
</main>
</body>
</html>
```